Website design needed for Renewable utilities company based in New Zealand.

Website design needed for Lanternvale Holdings based in New Zealand.

Please see attached logo.

We sell solar panels, vertical axis wind turbines, atmospheric water generators and other related equipment for those who don't have access or don't want to depend on the government, city councils for their utilities (power and water).

We like metallic texture, dark grey and purple, red or blue colours. The design should go well with the attached logo.

Target Market(s)

The Eco conscious

Industry/Entity Type

Government

Logo Text

Lanternvale Summit

Requirements
Must have
• Must Have:
- Metallic finish is a must.
- Design should fit around the attached logo well.
Nice to have
• Sharpe design prefred rather than rounded edges

```html
<!DOCTYPE html>
<html lang="en">
<head>
<meta charset="utf-8">
<title>Lanternvale Summit</title>
<link rel="stylesheet" href="https://fonts.googleapis.com/css2?family=Cabin:wght@400;600&family=Open+Sans:wght@300;400;600&family=Yanone+Kaffeesatz:wght@400;600&display=swap">
<style>
:root{
  --blue:#0a9ee0;
  --blue-dark:#0b86c4;
  --navy:#1b2a5c;
  --text:#222;
  --muted:#666;
  --page:#f1f1f1;
  --white:#fff;
  --line:#d4d4d4;
}
*{margin:0;padding:0;box-sizing:border-box}
html,body{width:1200px;height:1200px;overflow:hidden}
body{position:relative;background:var(--page);font-family:Arial,Helvetica,sans-serif;color:var(--text)}
.abs{position:absolute}
.header{left:0;top:0;width:1200px;height:182px;background:var(--white);border-bottom:1px solid #ddd}
.hero-band{left:0;top:182px;width:1200px;height:400px;background:linear-gradient(#e2e2e2,#ececec);border-bottom:1px solid #dadada}
.brand{left:118px;top:106px;display:flex;align-items:center;gap:12px}
.brand-mark{width:34px;height:34px;border-radius:50%;background:var(--blue)}
.brand-name{font-family:Cabin,sans-serif;font-size:27px;color:var(--blue);font-weight:400}
.call{right:116px;top:38px;display:flex;align-items:center;gap:10px;font-family:Cabin,sans-serif}
.call-label{font-size:20px;color:var(--navy);margin-top:8px}
.call-number{font-family:"Open Sans",sans-serif;font-size:33px;font-weight:300;color:#555;border-bottom:1px dotted #333;line-height:38px;letter-spacing:1px}
.connect{right:118px;top:105px;display:flex;align-items:center;gap:8px}
.connect-label{font-family:Cabin,sans-serif;font-size:18px;color:#888;margin-right:4px}
.social{width:35px;height:35px;background:linear-gradient(#fafafa,#e1e1e1);border:1px solid #d0d0d0}
.nav{left:112px;top:164px;width:971px;height:42px;background:linear-gradient(#15b0ef,var(--blue-dark));border-radius:10px;display:flex}
.nav a{color:var(--white);text-decoration:none;font-size:14px;display:flex;align-items:center;justify-content:center;border-right:1px solid #0678b0;box-shadow:1px 0 0 #3cc3f5}
.nav a:last-child{border:0;box-shadow:none}
.slider{left:112px;top:232px;width:974px;height:311px;background:var(--white);border:1px solid #dcdcdc}
.slide{left:6px;top:6px;width:958px;height:297px;background:linear-gradient(160deg,#1a3aa6 0%,#2c5fc9 40%,#1d2e80 100%)}
.slide-title{right:79px;top:22px;font-family:"Yanone Kaffeesatz",sans-serif;font-weight:600;font-size:52px;color:#4cc6f5;font-style:italic;line-height:1.1}
.slide-sub{right:39px;top:82px;font-family:"Yanone Kaffeesatz",sans-serif;font-size:38px;color:var(--white);line-height:1.1}
.arrow{width:46px;height:46px;border-radius:50%;background:linear-gradient(#fdfdfd,#d6d6d6);border:1px solid #bbb}
h2.section{font-family:Cabin,sans-serif;font-weight:400;font-size:24px;color:#333}
h2.section b{color:var(--blue);font-weight:600}
.welcome-title{left:120px;top:619px}
.photo-frame{left:120px;top:675px;width:181px;height:199px;background:var(--white);border:1px solid #d6d6d6}
.photo{left:5px;top:5px;width:169px;height:187px;background:linear-gradient(#6ab7ea 0%,#cfe7f5 55%,#9ccc3a 70%,#6fa823 100%)}
.welcome-text{left:320px;top:678px;width:442px;font-size:12px;line-height:20px;text-align:justify}
.welcome-text p+p{margin-top:20px}
.lead{color:var(--blue);font-weight:bold}
.divider{left:781px;top:605px;height:282px;border-left:1px dotted #bbb}
.testi-icon{left:822px;top:608px}
.testi-title{left:877px;top:619px;font-family:Cabin,sans-serif;font-weight:600;font-size:23px;color:var(--blue)}
.quote{font-family:Georgia,serif;font-size:40px;color:#aaa;line-height:1}
.testi-text{left:819px;top:665px;width:250px;font-family:"Open Sans",sans-serif;font-size:11px;line-height:20px;color:#444;text-align:justify;letter-spacing:.3px}
.testi-name{left:823px;top:817px;font-family:"Open Sans",sans-serif;font-weight:600;font-style:italic;font-size:15px;color:#666}
.testi-rule{left:815px;top:851px;width:275px;border-top:1px solid var(--line)}
.card{width:285px;height:189px;background:linear-gradient(#ffffff,#ececec);border:1px solid #dfdfdf;border-radius:14px;box-shadow:14px 8px 14px rgba(0,0,0,.08)}
.card h2{position:absolute;left:19px;top:17px}
.card-text{position:absolute;left:19px;top:60px;width:252px;font-size:12px;line-height:20px;text-align:justify}
.ticks{position:absolute;left:18px;top:66px;list-style:none;font-size:12px}
.ticks li{height:24px;display:flex;align-items:center;gap:8px}
.footer-line{left:0;top:1133px;width:1200px;border-top:1px solid #ddd}
.footer-nav{left:120px;top:1165px;display:flex;font-size:12.4px}
.footer-nav i{font-style:normal;margin:0 22px 0 16px}
.copyright{left:747px;top:1165px;font-size:12.4px}
</style>
</head>
<body>
<div class="abs header"></div>
<div class="abs hero-band"></div>

<div class="abs brand"><span class="brand-mark"></span><span class="brand-name">Lanternvale Summit</span></div>

<div class="abs call">
  <span class="call-label">Call No</span>
  <svg width="24" height="24" viewBox="0 0 24 24"><rect width="24" height="24" rx="4" fill="#1b4aa0"/><path d="M8 5c-1 1-2 2-1 5s4 7 7 8 4 0 5-1l-3-3-2 1c-1-1-3-3-4-5l1-2z" fill="#fff"/></svg>
  <span class="call-number">1300 555 0142</span>
</div>

<div class="abs connect">
  <span class="connect-label">Connect with us :-</span>
  <span class="social"></span><span class="social"></span><span class="social"></span><span class="social"></span>
</div>

<nav class="abs nav">
  <a style="width:128px">HOME</a>
  <a style="width:172px">PRODUCTS</a>
  <a style="width:172px">SERVIES</a>
  <a style="width:171px">ABOUT US</a>
  <a style="width:172px">SUPPORT</a>
  <a style="width:156px">CONTACT US</a>
</nav>

<div class="abs arrow" style="left:100px;top:344px"></div>
<div class="abs arrow" style="left:1053px;top:364px"></div>
<div class="abs slider">
  <div class="abs slide" role="img" aria-label="Rows of solar panels under a blue sky"></div>
  <div class="abs slide-title">Solar Panels</div>
  <div class="abs slide-sub">Simple Affordable Profitable</div>
</div>

<h2 class="abs section welcome-title">Welcome to <b>LANTERNVALE SUMMIT</b></h2>
<div class="abs photo-frame"><div class="abs photo" role="img" aria-label="Vertical axis wind turbine standing in a green field"></div></div>
<div class="abs welcome-text">
  <p><span class="lead">Lorem Ipsum is simply dummy text of the printing</span> and typesetting industry. Lorem Ipsum has been the industry's standard dummy text ever since the 1500s, when an unknown printer took a galley of type and scrambled it to make a type specimen book. It has survived not only five centuries, but also the leap into electronic typesetting, remaining essentially unchanged.</p>
  <p>It was popularised in the 1960s with the release of Pressmark sheets containing Lorem Ipsum passages, and more recently with desktop publishing software like Quillset Layout including versions of Lorem Ipsum.</p>
</div>

<div class="abs divider"></div>
<svg class="abs testi-icon" width="52" height="44" viewBox="0 0 52 44">
  <ellipse cx="38" cy="12" rx="13" ry="9" fill="none" stroke="#555" stroke-width="2"/>
  <line x1="32" y1="11" x2="44" y2="11" stroke="#555" stroke-width="1.5"/>
  <circle cx="14" cy="18" r="5" fill="#555"/>
  <path d="M4 40c0-10 4-14 10-14s10 4 10 14z" fill="#555"/>
</svg>
<div class="abs testi-title">TESTIMONIALS</div>
<div class="abs quote" style="left:796px;top:660px">&ldquo;</div>
<div class="abs testi-text">Lorem Ipsum is simply dummy text of the printing and typesetting industry. Lorem Ipsum has been the industry's standard dummy text ever since the 1500s, when an unknown printer took a galley of type and scrambled it to make a type specimen book. It has survived not only five centuries.</div>
<div class="abs quote" style="left:1052px;top:787px">&rdquo;</div>
<div class="abs testi-name">Mara</div>
<div class="abs testi-rule"></div>

<div class="abs card" style="left:119px;top:914px">
  <h2 class="section">Who We <b>Are ?</b></h2>
  <p class="card-text"><span class="lead">Lorem Ipsum is simply</span> dummy text of the printing and typesetting industry. Lorem Ipsum has been the industry's standard dummy text ever since the 1500s, when an unknown printer took a galley</p>
</div>
<div class="abs card" style="left:459px;top:914px">
  <h2 class="section" style="left:40px;top:20px">What We <b>Do ?</b></h2>
  <ul class="ticks">
    <li><svg width="15" height="12" viewBox="0 0 15 12"><path d="M1 6l4 4 9-9" fill="none" stroke="#0a9ee0" stroke-width="2.5"/></svg>Lorem Ipsum is simply dummy text</li>
    <li><svg width="15" height="12" viewBox="0 0 15 12"><path d="M1 6l4 4 9-9" fill="none" stroke="#0a9ee0" stroke-width="2.5"/></svg>The printing and typesetting industry.</li>
    <li><svg width="15" height="12" viewBox="0 0 15 12"><path d="M1 6l4 4 9-9" fill="none" stroke="#0a9ee0" stroke-width="2.5"/></svg>Dummy text ever since the 1500s,</li>
    <li><svg width="15" height="12" viewBox="0 0 15 12"><path d="M1 6l4 4 9-9" fill="none" stroke="#0a9ee0" stroke-width="2.5"/></svg>when an unknown printer took a galley</li>
  </ul>
</div>
<div class="abs card" style="left:789px;top:914px">
  <h2 class="section" style="left:18px;top:16px">Our <b>Products</b></h2>
  <p class="card-text" style="left:16px;top:68px"><span style="color:var(--blue)">Lorem Ipsum is simply</span> dummy text of the printing and typesetting industry. Lorem Ipsum has been the industry's standard dummy text ever since the 1500s, when an unknown printer took a galley</p>
</div>

<div class="abs footer-line"></div>
<div class="abs footer-nav">
  <span>Home</span><i>|</i><span>Products</span><i>|</i><span>Servies</span><i style="margin-left:38px">|</i><span>About Us</span><i style="margin-left:34px">|</i><span>Support</span><i>|</i><span>Contact Us</span>
</div>
<div class="abs copyright">Copyright (C) Lanternvale Summit 2004. All Rights Reserved</div>
</body>
</html>
```